Project Manager Business Card for Top Architectural Firm

Update and design a stunning Senior Project Manager Business Card

MARCO T. RUEDA II
Senior Project Manager

H A R B O R L I N E
A R C H I T E C T U R E L L C.
www.HarborlineCrestHouses.com
4217 NW 38th Ter. Suite 905
Miami, FL 33172
C: (305) 418-2273
mrueda.harborlinecresthouses@mailvista.net

Looking to have the logo to be UV Spot ink printed and to be prominent.

Target Market(s)

High end real estate architecture construction

Industry/Entity Type

Architect

Contact Information for Business Card

MARCO T. RUEDA II
Senior Project Manager

H A R B O R L I N E
Miami, FL 33172
C: (305) 418-2273

Font styles to use
Sans Serif

Colors

Designer to choose colors to be used in the design.

Requirements
Must have
• Prominent Logo

```html
<!DOCTYPE html>
<html lang="en">
<head>
<meta charset="utf-8">
<title>Harborline Architecture LLC – Business Card</title>
<link rel="stylesheet" href="https://fonts.googleapis.com/css2?family=Poiret+One&family=Michroma&family=Montserrat:wght@300;400&display=swap">
<style>
  :root {
    --stage: #2b2c30;
    --card-dark: #111113;
    --card-light: #ffffff;
    --ink: #151515;
    --ink-soft: #333336;
    --blue: #2f6bb0;
    --blue-light: #6fa6d6;
    --red: #c7302a;
    --red-dark: #8f1b1b;
    --white: #ffffff;
  }
  * { box-sizing: border-box; margin: 0; padding: 0; }
  html, body { width: 1200px; height: 901px; overflow: hidden; }
  body {
    background: var(--stage);
    display: flex;
    flex-direction: column;
    align-items: center;
    justify-content: center;
    gap: 36px;
  }
  .card {
    position: relative;
    width: 660px;
    height: 377px;
    border-radius: 22px;
    overflow: hidden;
  }

  /* Back of card */
  .card--back {
    background: var(--card-dark);
    display: flex;
    align-items: center;
    justify-content: center;
  }
  .brand {
    display: flex;
    flex-direction: column;
    align-items: center;
    gap: 14px;
  }
  .brand__dot {
    width: 64px;
    height: 64px;
    border-radius: 50%;
    background: var(--blue);
  }
  .brand__name {
    font-family: "Poiret One", sans-serif;
    color: var(--white);
    font-size: 46px;
    letter-spacing: 8px;
    line-height: 1;
    text-align: center;
  }
  .brand__sub {
    font-family: "Poiret One", sans-serif;
    color: var(--white);
    font-size: 15px;
    letter-spacing: 5px;
    text-align: center;
    margin-top: 6px;
  }

  /* Front of card */
  .card--front { background: var(--card-light); }
  .front__mark {
    position: absolute;
    right: 70px;
    top: 34px;
    width: 210px;
    height: 210px;
    border-radius: 50%;
    background: var(--blue);
  }
  .front__bar {
    position: absolute;
    right: 0;
    top: 232px;
    width: 200px;
    height: 22px;
    background: linear-gradient(90deg, var(--red-dark), var(--red));
  }
  .front__info {
    position: absolute;
    left: 44px;
    top: 60px;
  }
  .front__name-brand {
    font-family: "Poiret One", sans-serif;
    color: var(--ink);
    font-size: 52px;
    letter-spacing: 7px;
    line-height: 1;
  }
  .front__name-sub {
    font-family: "Poiret One", sans-serif;
    color: var(--ink);
    font-size: 15px;
    letter-spacing: 5px;
    margin-top: 6px;
  }
  .person__name {
    font-family: "Poiret One", sans-serif;
    color: var(--ink);
    font-size: 30px;
    letter-spacing: 1px;
    margin-top: 22px;
    line-height: 1;
  }
  .person__title {
    font-family: "Michroma", sans-serif;
    color: var(--ink);
    font-size: 11px;
    letter-spacing: 2px;
    margin-top: 8px;
  }
  .contact {
    list-style: none;
    margin-top: 22px;
    font-family: "Montserrat", sans-serif;
    font-weight: 300;
    font-size: 13px;
    color: var(--ink-soft);
    line-height: 1.55;
  }
  .front__band {
    position: absolute;
    left: 0;
    bottom: 0;
    width: 100%;
    height: 36px;
    background: linear-gradient(90deg, var(--blue) 0%, var(--blue) 55%, var(--blue-light) 100%);
    display: flex;
    align-items: center;
    padding-left: 44px;
    font-family: "Michroma", sans-serif;
    font-size: 11.5px;
    letter-spacing: 1px;
    color: var(--white);
  }
</style>
</head>
<body>
  <section class="card card--back" aria-label="Card back">
    <div class="brand">
      <div class="brand__dot"></div>
      <div>
        <div class="brand__name">HARBORLINE</div>
        <div class="brand__sub">ARCHITECTURE LLC.</div>
      </div>
    </div>
  </section>

  <section class="card card--front" aria-label="Card front">
    <div class="front__mark"></div>
    <div class="front__bar"></div>
    <div class="front__info">
      <div class="front__name-brand">HARBORLINE</div>
      <div class="front__name-sub">ARCHITECTURE LLC.</div>
      <div class="person__name">MARCO T. RUEDA II</div>
      <div class="person__title">SENIOR PROJECT MANAGER</div>
      <ul class="contact">
        <li>M: (305) 418-2273</li>
        <li>mrueda.harborlinecresthouses@mailvista.net</li>
        <li>www.HarborlineCrestHouses.com</li>
      </ul>
    </div>
    <div class="front__band">4217 NW 38TH TER. SUITE 905, MIAMI, FL 33172</div>
  </section>
</body>
</html>
```